Flyer for annual KESTREL SUMMIT 2020

I would like a church event flyer designed. The event is called "KESTREL SUMMIT 2020". I am looking for a professional, yet catchy design that uses our brand colors and logo creatively while communicating key information of the event effectively.

1. The logo is attached in two color formats. The designer has the choice to use them as he/she want.

2. The location of the event is: Harlow Community Center, 239 Fennimore Street, Portland, ME 04117

3. Time and date of event. The designer can organize and format the date and time as he/she pleases.
Thursday December 31st @ 6:30PM
Friday January 1st @ 6:30PM
Saturday 2nd @ 6:30PM
Sunday 3rd @ 4:30PM

4. The topic of the event is "In Fire and On Fire". The designer is free to use this phrase as he/she pleases to create a good composition.

5. Speaker: Prophet Marcus Olunde (2 pictures of the speaker to choose from are attached)

6. Contact information: contact@brightmeadowfold.org - Telephone number: 207 583 2914

7. I would also like the following three words on the flyer. These words describe the focus of the event: FIRE, REVIVAL, PROPHETIC

Target Market(s)

Young adults

Font styles to use
Sans Serif

Requirements
Must have
• Logo, speaker's picture
Should not have
• cross image, church image

```html
<!DOCTYPE html>
<html lang="en">
<head>
<meta charset="utf-8">
<title>Kestrel Summit 2020 Flyer</title>
<link rel="stylesheet" href="https://fonts.googleapis.com/css2?family=Rubik:wght@400;500;700;800&family=Montserrat:wght@400;500&family=Domine:wght@700&display=swap">
<style>
  :root {
    --navy: #0b3a62;
    --navy-deep: #082e50;
    --orange: #f7941d;
    --white: #ffffff;
    --ember: #5a1208;
    --page: #e9e9e9;
  }
  * { margin: 0; padding: 0; box-sizing: border-box; }
  html, body { width: 672px; height: 1200px; overflow: hidden; background: var(--page); }
  .flyer {
    position: absolute; left: 0; top: 124px; width: 672px; height: 952px;
    background: linear-gradient(180deg, var(--navy) 0%, var(--navy-deep) 100%);
    overflow: hidden; font-family: "Rubik", sans-serif; color: var(--white);
  }
  .speaker-photo { position: absolute; left: 0; top: 0; }
  .brand { position: absolute; left: 75px; top: 48px; display: flex; align-items: center; gap: 10px; }
  .brand-dot { width: 22px; height: 22px; border-radius: 50%; background: var(--orange); }
  .brand-name { font-family: "Rubik", sans-serif; font-weight: 500; font-size: 48px; letter-spacing: 1px; color: var(--white); }
  .title { position: absolute; left: 73px; top: 180px; line-height: 1; }
  .title-main { font-weight: 800; font-size: 60px; letter-spacing: -0.5px; }
  .title-sub { font-weight: 700; font-size: 38px; color: var(--orange); margin-top: 10px; }
  .title-year { font-weight: 800; font-size: 112px; letter-spacing: -3px; margin-top: 6px; }
  .info { position: absolute; left: 75px; width: 240px; font-size: 12.5px; line-height: 1.35; }
  .info-icon { position: absolute; left: -20px; top: 1px; }
  .location { top: 446px; }
  .location strong { font-weight: 700; display: block; }
  .rule { position: absolute; left: 75px; width: 236px; height: 1px; background: rgba(255,255,255,0.35); }
  .rule-a { top: 504px; } .rule-b { top: 581px; }
  .note { top: 520px; font-weight: 400; }
  .dates { top: 591px; }
  .dates span { color: var(--orange); font-weight: 500; }
  .theme-badge {
    position: absolute; left: 72px; top: 692px; width: 258px; height: 118px;
    border: 4px solid var(--orange); border-radius: 6px;
    background: radial-gradient(ellipse at center, #7a1c0a 0%, var(--ember) 70%, #3a0a04 100%);
    box-shadow: 0 0 22px 6px rgba(247,148,29,0.55);
    display: flex; align-items: center; justify-content: center; text-align: center;
    font-family: "Domine", serif; font-weight: 700; font-size: 28px; line-height: 1.05; color: var(--orange);
  }
  .speaker-tag { position: absolute; left: 337px; top: 748px; width: 335px; height: 76px; background: var(--orange); padding: 14px 0 0 28px; }
  .speaker-label { font-weight: 700; font-size: 14px; color: var(--navy); }
  .speaker-name { font-weight: 700; font-size: 25px; color: var(--white); margin-top: 1px; }
  .focus { position: absolute; left: 74px; top: 850px; display: flex; gap: 26px; align-items: center; }
  .focus-item { display: flex; align-items: center; gap: 8px; font-weight: 700; font-size: 29px; }
  .contact { position: absolute; left: 74px; top: 906px; display: flex; gap: 12px; align-items: center; font-family: "Montserrat", sans-serif; font-size: 16px; }
  .contact-item { display: flex; align-items: center; gap: 8px; }
</style>
</head>
<body>
<main class="flyer">
  <svg class="speaker-photo" width="672" height="952" viewBox="0 0 672 952" role="img" aria-label="Portrait of the speaker in an orange suit against a fire and orange backdrop">
    <defs>
      <linearGradient id="photo-tone" x1="0" y1="0" x2="1" y2="1">
        <stop offset="0" stop-color="#ffffff"/>
        <stop offset="0.25" stop-color="#f5a13a"/>
        <stop offset="0.6" stop-color="#c84a22"/>
        <stop offset="1" stop-color="#8e2c17"/>
      </linearGradient>
    </defs>
    <path d="M540 0 C470 40 450 160 500 260 C530 310 480 360 420 440 C370 520 360 640 380 748 L672 748 L672 0 Z" fill="url(#photo-tone)" stroke="#ffffff" stroke-width="3"/>
  </svg>

  <div class="brand"><span class="brand-dot"></span><span class="brand-name">CORVANE</span></div>

  <h1 class="title">
    <div class="title-main">KESTREL</div>
    <div class="title-sub">SUMMIT</div>
    <div class="title-year">2020</div>
  </h1>

  <p class="info location">
    <svg class="info-icon" width="14" height="16" viewBox="0 0 14 16"><path d="M7 1a5 5 0 0 0-5 5c0 4 5 9 5 9s5-5 5-9a5 5 0 0 0-5-5z" fill="none" stroke="#f7941d" stroke-width="1.6"/><circle cx="7" cy="6" r="1.8" fill="#f7941d"/></svg>
    The location of the event is:
    <strong>Harlow Community Center, 239 Fennimore Street, Portland, ME 04117</strong>
  </p>
  <div class="rule rule-a"></div>
  <p class="info note">Time and date of event. The designer can organize and format the date and time as he/she pleases</p>
  <div class="rule rule-b"></div>
  <p class="info dates">
    <svg class="info-icon" width="14" height="14" viewBox="0 0 14 14"><rect x="1" y="2" width="12" height="11" rx="1.5" fill="none" stroke="#f7941d" stroke-width="1.4"/><line x1="1" y1="5.5" x2="13" y2="5.5" stroke="#f7941d" stroke-width="1.4"/></svg>
    <span>Thursday December</span> 31st @ 6:30PM<br>
    <span>Friday January</span> 1st @ 6:30PM<br>
    <span>Saturday</span> 2nd @ 6:30PM<br>
    <span>Sunday</span> 3rd @ 4:30PM
  </p>

  <div class="theme-badge">IN FIRE AND<br>ON FIRE</div>

  <div class="speaker-tag">
    <div class="speaker-label">SPEAKER:</div>
    <div class="speaker-name">Prophet Marcus Olunde</div>
  </div>

  <div class="focus">
    <div class="focus-item"><svg width="22" height="32" viewBox="0 0 22 32"><path d="M11 1C14 9 21 12 21 21a10 10 0 0 1-20 0c0-6 4-8 5-13 2 3 2 6 4 7 1-5 1-9 1-14z" fill="#f7941d"/></svg>FIRE</div>
    <div class="focus-item"><svg width="32" height="30" viewBox="0 0 32 30"><circle cx="16" cy="8" r="5" fill="#f7941d"/><path d="M4 12l6 4v12h12V16l6-4-2 10-4 2v4H10v-4l-4-2z" fill="#f7941d"/></svg>REVIVAL</div>
    <div class="focus-item"><svg width="26" height="32" viewBox="0 0 26 32"><circle cx="13" cy="9" r="6" fill="#f7941d"/><path d="M2 31c0-9 5-13 11-13s11 4 11 13z" fill="#f7941d"/></svg>PROPHETIC</div>
  </div>

  <div class="contact">
    <div class="contact-item"><svg width="16" height="16" viewBox="0 0 16 16"><path d="M3 1l3 3-2 2c1 2 3 4 5 5l2-2 3 3-2 3C7 15 1 9 1 3z" fill="#f7941d"/></svg>Telephone number: 207 583 2914</div>
    <div class="contact-item"><svg width="15" height="13" viewBox="0 0 15 13"><rect x="0.8" y="0.8" width="13.4" height="11.4" rx="1.5" fill="none" stroke="#f7941d" stroke-width="1.5"/><path d="M1 2l6.5 5L14 2" fill="none" stroke="#f7941d" stroke-width="1.5"/></svg>contact@brightmeadowfold.org</div>
  </div>
</main>
</body>
</html>
```